Stationery Design Project

Our company is "Meridal Systems" and we have a product called "quillbrook.com". The product is an online accounting software for businesses. We want to communicate that our software will help business owners to be more efficient and help them track their finances better. Quillbrook.com is basically a simple version of ledgerpine.

"We want a unique and creative design which will surprise our customer."

NAME CARD = QUILLBROOK
We want a quillbrook name card NOT MERIDAL SYSTEMS.

For the content of the name card, please make sure it fit with a long name like the following:

Roswin Halim Alias Roswin
Developer Specialist
T: (021) 4172 3846
F: (021) 4172 3847
E: customer.service@mrd.co.id

I need you to put it the following information to the name card

"quillbrook"
- moto is "automate your businesses"
- website "www.quillbrook.com"
- quillbrook is a "Web Accounting Software"
- product of "Meridal Systems"

LETTERHEAD, ENVELOPE, FOLDER = MERIDAL SYSTEMS
Other than name card we wanted you to design for us; letterhead, envelope and folder. In letterhead, envelope and folder it should ONLY contain the following information ("Meridal Systems").
PLEASE BE SURE YOU ARE NOT PUTTING "QUILLBROOK LOGO" IN LETTERHEAD, ENVELOPE AND FOLDER.

"Meridal Systems"
Address:
Ruko Harbor Plaza Blok. D No. 18
Jl. Kembangsari No. 47
Jakarta
Kalideres, 11840
Indonesia

Web Address: mrd.co.id

T: (021) 4172 3846
F: (021) 4172 3847

Target Market(s)

Business Owners, Accountant, Auditor, Tax Consultant

Industry/Entity Type

Accounting

Requirements
Must have
• .

```html
<!DOCTYPE html>
<html lang="en">
<head>
<meta charset="utf-8">
<title>Meridal Systems Letterhead</title>
<link rel="stylesheet" href="https://fonts.googleapis.com/css2?family=Belleza&display=swap">
<style>
  :root {
    --canvas: #ffffff;
    --canvas-edge: #d4d4d4;
    --sheet: #ffffff;
    --sheet-edge: #bdbdbd;
    --band-top: #1a2e0e;
    --band-mid: #47a404;
    --band-bottom: #c2ff00;
    --mark: #4a9a1a;
    --brand-ink: #4b5761;
    --text-ink: #2a2a2a;
  }
  html, body {
    margin: 0;
    padding: 0;
    width: 1200px;
    height: 900px;
    overflow: hidden;
    background: var(--canvas);
  }
  .canvas {
    position: relative;
    width: 1200px;
    height: 900px;
    box-sizing: border-box;
    border: 1px solid var(--canvas-edge);
    background: var(--canvas);
    font-family: "Belleza", sans-serif;
  }
  .letterhead {
    position: absolute;
    left: 302px;
    top: 29px;
    width: 596px;
    height: 842px;
    box-sizing: border-box;
    border: 1px solid var(--sheet-edge);
    background: var(--sheet);
  }
  .side-band {
    position: absolute;
    left: -1px;
    top: -1px;
    width: 46px;
    height: 842px;
    background: linear-gradient(to bottom, var(--band-top) 0%, #2a6108 30%, var(--band-mid) 55%, #8fdb00 80%, var(--band-bottom) 100%);
  }
  .brand {
    position: absolute;
    left: 85px;
    top: 40px;
    display: flex;
    align-items: center;
    gap: 8px;
  }
  .brand-dot {
    width: 50px;
    height: 50px;
    border-radius: 50%;
    background: var(--mark);
  }
  .brand-name {
    font-size: 19px;
    letter-spacing: 0.5px;
    color: var(--brand-ink);
    white-space: nowrap;
  }
  .address {
    position: absolute;
    right: 44px;
    top: 33px;
    margin: 0;
    text-align: right;
    font-style: normal;
    font-size: 9px;
    line-height: 10.9px;
    color: var(--text-ink);
  }
  .contact-line {
    position: absolute;
    left: 92px;
    right: 44px;
    top: 790px;
    display: flex;
    font-size: 9px;
    color: var(--text-ink);
  }
  .contact-line .phone { width: 173px; }
  .contact-line .fax { flex: 1; }
</style>
</head>
<body>
<div class="canvas">
  <div class="letterhead">
    <div class="side-band"></div>

    <div class="brand">
      <span class="brand-dot"></span>
      <span class="brand-name">MERIDAL SYSTEMS</span>
    </div>

    <address class="address">
      Ruko Harbor Plaza Blok D No. 18<br>
      Jl. Kembangsari No. 47<br>
      Jakarta<br>
      Kalideres, 11840<br>
      Indonesia<br>
      Web Address: mrd.co.id
    </address>

    <div class="contact-line">
      <span class="phone">T: (021) 4172 3846</span>
      <span class="fax">F: (021) 4172 3847</span>
      <span class="email">E: customer.service@mrd.co.id</span>
    </div>
  </div>
</div>
</body>
</html>
```